Reclaimed Tavern & Inn Kit need a website

We need a website designed and created to facilitate us to promote & sell our products online. We buy excess / clearance lots of pub, cafe, restaurant & hotel furniture and equipment (usually from businesses that have excess inventory after a refurb or have closed down). We then sell these to other businesses mainly through our Facebook page "Reclaimed Tavern & Inn Kit" but the process is cumbersome for the following reasons:
1) We dont have a stock list and images as it changes daily and people can only rely on recent posts and dont know if something is for sale still or is sold
2) we do not have the facility to sell online.

We are open to ideas and design concepts

We already have a logo & stationery deisgned

its probably best to look through our Facebook page to better understand what we do

We would consider a catalogue / by department / category user interface such as:
https://rehomed-taproom-gear.co.uk/

Our preference would be to change / delete / update stock via smartphone to best facilitate the maintenance of the website which i will do myself

Suggested categories would include:
Bar Furniture
Bar Equipment
Restaurant Furniture
Catering Equipment
Bedroom Furniture
Miscellaneous

Sub categories would include:
Bar Furniture:
Bar Stools
Bar Tables
Benches
Tub chairs
Arm chairs
Pub Mirrors
Pub Signs
Pub Memorabilia

Bar Equipment:
Bottle Coolers
Ice Machines
Glass Washers
Tills
Lighting
Sound
Wireless waiter
Glassware
Taps
Line coolers
Snooker tables
Pool tables
gaming machines

Restaurant Furniture:
Tables
Chairs
Wine racks
Dressers
Couches
Bench seating
Tub Chairs
Arm chairs
High chairs
Menu boards
Mirrors
Pictures

Catering Equipment:
Fridges
Freezers
Ovens
Cookers
Fryers
Carvery units
Hot display units
Refrigerated displays
Sinks
Stainless steel units
Microwaves
Mixers
Crockery
Cutlery
Utensils
Glassware

Bedroom Furniture:
Beds
Headboards
Wardrobes
Lockers
Dressing Tables
Mirrors
Lamps
Pictures

Profit sharing schemes:
Pool Tables
Juke Boxes
Gaming Machines

Target Market(s)

Pubs
Restaurants
cafes
guest houses
hotels

Industry/Entity Type

Hospitality

Number of Pages Required

5+ page

Colors

Designer to choose colors to be used in the design.

Requirements
Must have
• Website featuring our categories of stock to sell
Nice to have
• Ecommerce option
Should not have
• just a front page

```html
<!DOCTYPE html>
<html lang="en">
<head>
<meta charset="utf-8">
<title>Reclaimed Tavern &amp; Inn Kit</title>
<link href="https://fonts.googleapis.com/css2?family=Arimo:wght@400;700&family=Libre+Baskerville:wght@400;700&display=swap" rel="stylesheet">
<style>
:root{
  --red:#b5121b;
  --red-dark:#8e1016;
  --ink:#1d1d1d;
  --grey:#555;
  --white:#fff;
  --footer-bar:#2a2a2a;
  --sans:"Arimo",Arial,sans-serif;
  --serif:"Libre Baskerville",Georgia,serif;
}
*{margin:0;padding:0;box-sizing:border-box}
html,body{width:1200px;height:1200px;overflow:hidden;background:var(--white)}
.stage{position:relative;width:1500px;height:1500px;transform:scale(.8);transform-origin:0 0;font-family:var(--sans);color:var(--ink)}
.abs{position:absolute}
.brand{left:571px;width:357px;top:0;text-align:center}
.brand-mark{display:inline-block;width:14px;height:14px;background:var(--red);margin-top:22px}
.brand-name{font-family:var(--serif);font-weight:700;font-size:12.5px;margin-top:17px;letter-spacing:.2px;color:var(--ink)}
.brand-rule{position:absolute;left:50px;right:50px;top:44px;height:1px;background:var(--red)}
.nav{left:571px;top:80px;width:357px;height:22px;background:var(--red);color:var(--white);font-size:6px;font-weight:700}
.nav span{position:absolute;top:8px}
.nav .mini{font-size:3px;top:15px;font-weight:400}
.nav svg{position:absolute;top:6px}
.hero{left:571px;top:102px;width:357px;height:155px;background:linear-gradient(180deg,#5a2a2c 0%,#4a3322 35%,#6b4a2c 55%,#3a2a22 100%)}
.hero-title{position:absolute;left:0;right:0;top:89px;text-align:center;color:var(--white);font-weight:700;font-size:10px;letter-spacing:.3px}
.hero-btn{position:absolute;left:158px;top:106px;width:48px;height:14px;background:var(--red);color:var(--white);font-size:4.2px;text-align:center;line-height:5px;padding-top:2px}
.hero svg{position:absolute;top:131px}
.dots span{position:absolute;top:266px;height:1.5px;width:49px;background:var(--ink)}
.dots .on{background:var(--red)}
.cat-head{left:571px;width:342px;top:283px;text-align:center;font-size:8px}
.section-title{font-size:8px}
.row{display:flex;gap:15px}
.card{width:69px;text-align:center}
.card .photo{width:69px;height:62px}
.card .name{font-size:6px;margin-top:10px;color:#333}
.card .desc{font-size:4.1px;line-height:6px;margin-top:2px;color:#333}
.card .price{font-size:4.2px;color:var(--red);margin-top:3px}
.card .add{display:inline-block;width:38px;height:11px;background:var(--red);color:var(--white);font-size:4.2px;line-height:11px;margin-top:3px}
.see-all{width:51px;height:14px;background:var(--red);color:var(--white);font-size:5.5px;text-align:center;line-height:14px}
.footer{left:571px;top:1336px;width:357px;height:142px;background:radial-gradient(circle at 30% 40%,#b3151d,#8a0f15)}
.foot-logo{position:absolute;left:44px;top:0;width:100px;height:32px;background:var(--white);border-radius:0 0 3px 3px;text-align:center}
.foot-logo i{display:inline-block;width:7px;height:7px;background:var(--red);margin-top:7px}
.foot-logo b{display:block;font-family:var(--serif);font-size:4.3px;margin-top:6px;color:var(--ink)}
.serif-w{font-family:var(--serif);color:var(--white);font-weight:700;position:absolute}
.pill{position:absolute;height:13px;background:var(--white);border-radius:2px;font-family:var(--serif);font-weight:700;font-size:4.3px;text-align:center;line-height:13px;color:var(--red-dark)}
.scheme{position:absolute;width:64px;height:37px;border:1px solid var(--white)}
.scheme-label{position:absolute;font-family:var(--serif);color:var(--white);font-size:3.6px;width:64px;text-align:center}
.copy{left:571px;top:1478px;width:357px;height:22px;background:var(--footer-bar);color:var(--white);font-size:5px;line-height:22px;padding-left:9px}
.copy em{font-style:normal;color:var(--red)}
.social{position:absolute;right:18px;top:3px;width:16px;height:16px;border-radius:50%;background:#3b5a98}
</style>
</head>
<body>
<div class="stage">

  <header class="brand abs">
    <span class="brand-mark"></span>
    <div class="brand-rule"></div>
    <div class="brand-name">RECLAIMED TAVERN &amp; INN KIT</div>
  </header>

  <nav class="nav abs">
    <span style="left:42px">ALL PRODUCTS</span>
    <span style="left:100px">ABOUT US</span>
    <span style="left:142px">CONTACT US</span>
    <svg style="left:193px" width="8" height="8" viewBox="0 0 8 8"><circle cx="3.2" cy="3.2" r="2.2" fill="none" stroke="#fff" stroke-width="1"/><path d="M5 5l2.3 2.3" stroke="#fff" stroke-width="1"/></svg>
    <svg style="left:211px" width="9" height="8" viewBox="0 0 9 8"><path d="M0 1h2l1.2 4h4.3L8.5 2H2.6" fill="none" stroke="#fff" stroke-width=".9"/><circle cx="3.8" cy="6.8" r=".8" fill="#fff"/><circle cx="7" cy="6.8" r=".8" fill="#fff"/></svg>
    <svg style="left:244px" width="7" height="7" viewBox="0 0 7 7"><circle cx="3.5" cy="2" r="1.8" fill="#fff"/><path d="M0 7a3.5 3 0 0 1 7 0z" fill="#fff"/></svg>
    <span class="mini" style="left:236px">MY ACCOUNT</span>
    <svg style="left:278px" width="7" height="7" viewBox="0 0 7 7"><circle cx="3.5" cy="2" r="1.8" fill="#fff"/><path d="M0 7a3.5 3 0 0 1 7 0z" fill="#fff"/></svg>
    <span class="mini" style="left:265px">CREATE ACCOUNT</span>
    <svg style="left:306px" width="6" height="7" viewBox="0 0 6 7"><rect x="0" y="3" width="6" height="4" fill="#fff"/><path d="M1.3 3V2a1.7 1.7 0 0 1 3.4 0v1" fill="none" stroke="#fff" stroke-width=".8"/></svg>
    <span class="mini" style="left:304px">LOGIN</span>
  </nav>

  <section class="hero abs" role="img" aria-label="Photo of a pub bar counter with wooden stools and a barrel">
    <div class="hero-title">FEATURED PRODUCTS</div>
    <div class="hero-btn">CHECK ALL<br>CATEGORIES</div>
    <svg style="left:20px" width="8" height="12" viewBox="0 0 8 12"><path d="M7 1L2 6l5 5" fill="none" stroke="#fff" stroke-width="1"/></svg>
    <svg style="left:330px" width="8" height="12" viewBox="0 0 8 12"><path d="M1 1l5 5-5 5" fill="none" stroke="#fff" stroke-width="1"/></svg>
  </section>

  <div class="dots">
    <span class="on" style="left:669px"></span>
    <span style="left:732px"></span>
    <span style="left:790px"></span>
  </div>

  <h2 class="cat-head abs" style="font-weight:400">CATEGORIES</h2>

  <!-- Bar Furniture -->
  <h3 class="section-title abs" style="left:590px;top:305px;font-weight:400">Bar Furniture</h3>
  <div class="row abs" style="left:590px;top:323px">
    <div class="card"><div class="photo" role="img" aria-label="Round bar table with blue top" style="background:linear-gradient(#4a3a3a,#2f5f7a 55%,#3a2a22)"></div><div class="name">Lorem Ipsum</div><div class="desc">Lorem ipsum dolor sit amet,<br>consectetur adipiscing elit, sed<br>do eiusmod tempor incididunt</div><div class="price">$100</div><div class="add">Add to Cart</div></div>
    <div class="card"><div class="photo" role="img" aria-label="Cream round tables" style="background:linear-gradient(#6a5a4a,#d9c9ae 55%,#5a4030)"></div><div class="name">Lorem Ipsum</div><div class="desc">Lorem ipsum dolor sit amet,<br>consectetur adipiscing elit, sed<br>do eiusmod tempor incididunt</div><div class="price">$100</div><div class="add">Add to Cart</div></div>
    <div class="card"><div class="photo" role="img" aria-label="Leather tub chairs" style="background:linear-gradient(#3a3020,#b59a5a 60%,#4a3a25)"></div><div class="name">Lorem Ipsum</div><div class="desc">Lorem ipsum dolor sit amet,<br>consectetur adipiscing elit, sed<br>do eiusmod tempor incididunt</div><div class="price">$100</div><div class="add">Add to Cart</div></div>
    <div class="card"><div class="photo" role="img" aria-label="Green upholstered chairs" style="background:linear-gradient(#6a6a50,#9aa04a 55%,#4a4a30)"></div><div class="name">Lorem Ipsum</div><div class="desc">Lorem ipsum dolor sit amet,<br>consectetur adipiscing elit, sed<br>do eiusmod tempor incididunt</div><div class="price">$100</div><div class="add">Add to Cart</div></div>
  </div>
  <div class="see-all abs" style="left:726px;top:473px">SEE ALL</div>

  <!-- Bar Equipment -->
  <h3 class="section-title abs" style="left:590px;top:508px;font-weight:400">Bar Equipment</h3>
  <div class="row abs" style="left:590px;top:529px">
    <div class="card"><div class="photo" role="img" aria-label="Snooker table" style="background:linear-gradient(#7a2a20,#a0602a 45%,#2f7a3a)"></div><div class="name">Lorem Ipsum</div><div class="desc">Lorem ipsum dolor sit amet,<br>consectetur adipiscing elit, sed<br>do eiusmod tempor incididunt</div><div class="price">$100</div><div class="add">Add to Cart</div></div>
    <div class="card"><div class="photo" role="img" aria-label="Dartboard" style="background:linear-gradient(#1f3a6a,#2a2a3a 50%,#7a2020)"></div><div class="name">Lorem Ipsum</div><div class="desc">Lorem ipsum dolor sit amet,<br>consectetur adipiscing elit, sed<br>do eiusmod tempor incididunt</div><div class="price">$100</div><div class="add">Add to Cart</div></div>
    <div class="card"><div class="photo" role="img" aria-label="Gaming machines" style="background:linear-gradient(#2a1a1a,#8a2a2a 50%,#1a1a1a)"></div><div class="name" style="margin-top:14px">Lorem Ipsum</div><div class="desc">Lorem ipsum dolor sit amet,<br>consectetur adipiscing elit, sed<br>do eiusmod tempor incididunt</div><div class="price">$100</div><div class="add">Add to Cart</div></div>
    <div class="card"><div class="photo" role="img" aria-label="Gaming machine" style="background:linear-gradient(#1a1a1a,#a02a20 50%,#2a1a1a)"></div><div class="name">Lorem Ipsum</div><div class="desc">Lorem ipsum dolor sit amet,<br>consectetur adipiscing elit, sed<br>do eiusmod tempor incididunt</div><div class="price">$100</div><div class="add">Add to Cart</div></div>
  </div>
  <div class="see-all abs" style="left:724px;top:674px">SEE ALL</div>

  <!-- Restaurant Furniture -->
  <h3 class="section-title abs" style="left:591px;top:713px;font-weight:400">Restaurant Furniture</h3>
  <div class="row abs" style="left:590px;top:732px">
    <div class="card"><div class="photo" role="img" aria-label="Restaurant booth seating" style="background:linear-gradient(#8a8a8a,#4a3a3a 55%,#2a2020)"></div><div class="name">Lorem Ipsum</div><div class="desc">Lorem ipsum dolor sit amet,<br>consectetur adipiscing elit, sed<br>do eiusmod tempor incididunt</div><div class="price">$100</div><div class="add">Add to Cart</div></div>
    <div class="card"><div class="photo" role="img" aria-label="Wooden bar stools" style="background:linear-gradient(#7a7a6a,#5a3a25 55%,#3a2a20)"></div><div class="name">Lorem Ipsum</div><div class="desc">Lorem ipsum dolor sit amet,<br>consectetur adipiscing elit, sed<br>do eiusmod tempor incididunt</div><div class="price">$100</div><div class="add">Add to Cart</div></div>
    <div class="card"><div class="photo" role="img" aria-label="Dining chairs" style="background:linear-gradient(#8a8a80,#5a5048 55%,#2a2a2a)"></div><div class="name">Lorem Ipsum</div><div class="desc">Lorem ipsum dolor sit amet,<br>consectetur adipiscing elit, sed<br>do eiusmod tempor incididunt</div><div class="price">$100</div><div class="add">Add to Cart</div></div>
    <div class="card"><div class="photo" role="img" aria-label="Upholstered high stools" style="background:linear-gradient(#6a6a6a,#8a7a60 55%,#2a2520)"></div><div class="name">Lorem Ipsum</div><div class="desc">Lorem ipsum dolor sit amet,<br>consectetur adipiscing elit, sed<br>do eiusmod tempor incididunt</div><div class="price">$100</div><div class="add">Add to Cart</div></div>
  </div>
  <div class="see-all abs" style="left:724px;top:874px">SEE ALL</div>

  <!-- Catering Equipment -->
  <h3 class="section-title abs" style="left:591px;top:918px;font-weight:400">Catering Equipment</h3>
  <div class="row abs" style="left:590px;top:939px">
    <div class="card"><div class="photo" role="img" aria-label="Black upright fridge" style="background:linear-gradient(#4a4a4a,#1f1f1f 60%,#5a5a5a)"></div><div class="name">Lorem Ipsum</div><div class="desc">Lorem ipsum dolor sit amet,<br>consectetur adipiscing elit, sed<br>do eiusmod tempor incididunt</div><div class="price">$100</div><div class="add">Add to Cart</div></div>
    <div class="card"><div class="photo" role="img" aria-label="Glass door display fridge" style="background:linear-gradient(#9a9a9a,#5a5a5a 50%,#7a7a7a)"></div><div class="name">Lorem Ipsum</div><div class="desc">Lorem ipsum dolor sit amet,<br>consectetur adipiscing elit, sed<br>do eiusmod tempor incididunt</div><div class="price">$100</div><div class="add">Add to Cart</div></div>
    <div class="card"><div class="photo" role="img" aria-label="Stainless steel counter unit" style="background:linear-gradient(#5a5a5a,#b0b0b0 50%,#6a6a6a)"></div><div class="name">Lorem Ipsum</div><div class="desc">Lorem ipsum dolor sit amet,<br>consectetur adipiscing elit, sed<br>do eiusmod tempor incididunt</div><div class="price">$100</div><div class="add">Add to Cart</div></div>
    <div class="card"><div class="photo" role="img" aria-label="Stainless steel display unit" style="background:linear-gradient(#6a6a6a,#d0d0d0 50%,#4a4a4a)"></div><div class="name">Lorem Ipsum</div><div class="desc">Lorem ipsum dolor sit amet,<br>consectetur adipiscing elit, sed<br>do eiusmod tempor incididunt</div><div class="price">$100</div><div class="add">Add to Cart</div></div>
  </div>
  <div class="see-all abs" style="left:727px;top:1085px">SEE ALL</div>

  <!-- Bedroom Furniture -->
  <h3 class="section-title abs" style="left:589px;top:1130px;font-weight:400">Bedroom Furniture</h3>
  <div class="row abs" style="left:588px;top:1151px">
    <div class="card"><div class="photo" role="img" aria-label="Grey armchair" style="background:linear-gradient(#c0c0bc,#9a9a96 60%,#7a7a76)"></div><div class="name">Lorem Ipsum</div><div class="desc">Lorem ipsum dolor sit amet,<br>consectetur adipiscing elit, sed<br>do eiusmod tempor incididunt</div><div class="price">$100</div><div class="add">Add to Cart</div></div>
    <div class="card"><div class="photo" role="img" aria-label="Red armchair with cushion" style="background:linear-gradient(#6a4a3a,#8a2a2a 55%,#5a3a2a)"></div><div class="name">Lorem Ipsum</div><div class="desc">Lorem ipsum dolor sit amet,<br>consectetur adipiscing elit, sed<br>do eiusmod tempor incididunt</div><div class="price">$100</div><div class="add">Add to Cart</div></div>
    <div class="card"><div class="photo" role="img" aria-label="Stacked beige cushions" style="background:linear-gradient(#b0a89a,#8a7e70 55%,#a09888)"></div><div class="name">Lorem Ipsum</div><div class="desc">Lorem ipsum dolor sit amet,<br>consectetur adipiscing elit, sed<br>do eiusmod tempor incididunt</div><div class="price">$100</div><div class="add">Add to Cart</div></div>
    <div class="card"><div class="photo" role="img" aria-label="Patterned seat cushions" style="background:linear-gradient(#7a5a6a,#9a6a7a 55%,#5a4a5a)"></div><div class="name">Lorem Ipsum</div><div class="desc">Lorem ipsum dolor sit amet,<br>consectetur adipiscing elit, sed<br>do eiusmod tempor incididunt</div><div class="price">$100</div><div class="add">Add to Cart</div></div>
  </div>
  <div class="see-all abs" style="left:727px;top:1298px">SEE ALL</div>

  <footer class="footer abs">
    <div class="foot-logo"><i></i><b>RECLAIMED TAVERN &amp; INN KIT</b></div>
    <div class="serif-w" style="left:42px;top:45px;font-size:5px">WE BUY CLEARANCE LOTS FROM:</div>
    <div class="pill" style="left:8px;top:63px;width:56px">HOTELS</div>
    <div class="pill" style="left:67px;top:63px;width:55px">RESTAURANTS</div>
    <div class="pill" style="left:125px;top:63px;width:56px">CAFES</div>
    <div class="pill" style="left:37px;top:86px;width:55px">BARS</div>
    <div class="pill" style="left:95px;top:86px;width:56px">TAKE-AWAYS</div>
    <div class="serif-w" style="left:16px;top:111px;font-size:5.2px">TURN YOUR EXCESS INVENTORY INTO CASH!</div>
    <div class="serif-w" style="left:21px;top:119px;font-size:4.6px;font-weight:400">Call Declan @ 087 555 0142 and we will arrange a viewing.</div>

    <div class="serif-w" style="left:207px;top:21px;font-size:4.8px">PROFIT SHARE SCHEMES AVIALABLE ON:</div>
    <div class="scheme" role="img" aria-label="Pool table" style="left:204px;top:34px;background:linear-gradient(#3a3a3a,#2f8a3a)"></div>
    <div class="scheme-label" style="left:204px;top:73px">POOL TABLES</div>
    <div class="scheme" role="img" aria-label="Juke box" style="left:276px;top:34px;background:linear-gradient(#3a2a4a,#b0702a)"></div>
    <div class="scheme-label" style="left:276px;top:73px">JUKE BOXES</div>
    <div class="scheme" role="img" aria-label="Gaming machines" style="left:204px;top:82px;background:linear-gradient(#1a1a2a,#3a4a7a)"></div>
    <div class="scheme-label" style="left:204px;top:120px">GAMING MACHINES</div>
    <div class="scheme" style="left:278px;top:84px;width:59px;height:20px;background:var(--red);text-align:center">
      <div class="serif-w" style="position:static;font-size:4px;margin-top:4px">GIFT<br>VOUCHER</div>
    </div>
    <div class="serif-w" style="left:276px;top:106px;font-size:3.6px;font-weight:400;width:80px;line-height:5px">€100 voucher available for<br>every machine sited this year</div>
  </footer>

  <div class="copy abs">Copyright 2018 All Rights Reserved &nbsp;<em>Mill Lane, Ballyorrin, Co. Carrow</em> &nbsp;R99 T412 &nbsp; Call: 057 555 0198
    <span class="social"></span>
  </div>

</div>
</body>
</html>
```